Website design for respected, long standing real estate development company in Central Oregon

Uncoded PSD design only. Homepage and one interior sample page.

Updated website design needed for Fenwick Holdings, one of Central Oregon’s oldest and most respected real estate development companies. They develop communities that focus on natural beauty and upscale amenities.

They need a website that features their long, unique history and their current efforts to build smart, healthy and livable communities. They need to tell their story to those who aren't familiar with the company. They need to build credibility and set themselves apart from other real estate development companies.

Current site: http://fenwick-holdings.example/

Target Market(s)

Target market is people who are new or plan to relocate to Central Oregon and are researching communities they want to live in.
Secondary markets are potential project partners, and the media. They need to build credibility with these audiences.
The site also needs to be easy to use for non-profits seeking contributions.

Industry/Entity Type

Real Estate Development

Number of Pages Required

2 page

Font styles to use
Sans Serif

Requirements
Must have
• Must have simple, user-friendly navigation with organized content.
• Design must be fresh, light and modern.
• Design must use great, high impact imagery that promotes the Central Oregon lifestyle.
• Design must highlight current and future communities and encourage click-throughs to those specific websites.
• Include video element.
• Include social links.
• Do not use dummy copy/lorum ipsum. Use copy from the current site instead. Use correct phone number, address, etc.
Should not have
• Lorum ipsum/dummy copy

```html
<!DOCTYPE html>
<html lang="en">
<head>
<meta charset="utf-8">
<title>Fenwick Holdings Corporation</title>
<link rel="stylesheet" href="https://fonts.googleapis.com/css2?family=Josefin+Sans:wght@400;600;700&family=Lato:wght@400;700&display=swap">
<style>
:root{
  --plum:#4a2239;
  --plum-dark:#3d1c30;
  --ink:#2a2a2a;
  --muted:#777;
  --rule:#cfcfcf;
  --panel:#f3f3f3;
  --white:#fff;
  --social:#8e7286;
}
*{margin:0;padding:0;box-sizing:border-box}
html,body{width:762px;height:1200px;overflow:hidden}
body{position:relative;background:var(--white);font-family:"Lato",Arial,sans-serif;color:var(--ink)}
.abs{position:absolute}

.site-header{left:0;top:0;width:762px;height:94px;background:linear-gradient(#f7f7f7,#d8d8d8)}
.util-links{right:42px;top:8px;display:flex;gap:24px;font-size:8px;color:#333}
.brand{left:264px;top:16px;display:flex;align-items:center;gap:8px}
.brand-mark{width:30px;height:30px;background:var(--plum)}
.brand-name{font-weight:700;font-size:14px;color:#555;margin-top:12px}

.main-nav{left:30px;top:67px;width:701px;height:56px;background:var(--plum);border-radius:3px;display:flex;align-items:center;z-index:3;font-size:8.6px;font-weight:700;color:var(--white);letter-spacing:-.1px}
.main-nav a{display:block;padding:0 13.6px;line-height:56px;white-space:nowrap}
.main-nav a.active{background:var(--white);color:var(--plum);margin-left:22px;padding:0 13px;font-weight:400}

.hero{left:0;top:94px;width:762px;height:374px;background:linear-gradient(180deg,#9ab7cf 0%,#c6b48e 28%,#9b8665 45%,#6f8a3e 62%,#4f7a2a 80%,#8e8c82 100%)}
.hero-title{left:476px;top:342px;width:286px;height:84px;background:var(--plum);color:var(--white);font-family:"Josefin Sans",Arial,sans-serif;font-weight:700;font-size:30px;line-height:90px;padding-left:14px;white-space:nowrap}
.hero-arrows{left:364px;top:450px;width:42px;height:18px;background:#eee;display:flex;justify-content:center;align-items:center;gap:6px}

.welcome-title{left:30px;top:498px;width:701px;height:24px;display:flex;align-items:center;gap:8px;font-family:"Josefin Sans",Arial,sans-serif;font-weight:700;font-size:17px;color:#222;white-space:nowrap}
.welcome-title::before,.welcome-title::after{content:"";flex:1;height:1px;background:var(--rule)}
.welcome-title span{color:var(--plum);margin-left:5px}
.welcome-text{left:70px;top:540px;width:622px;text-align:center;font-size:7.4px;line-height:14px;color:#444}
.btn{background:var(--plum);color:var(--white);font-size:7.4px;display:flex;align-items:center;justify-content:center;border-radius:2px}
.welcome-btn{left:340px;top:598px;width:82px;height:24px}

.developments{left:0;top:643px;width:762px;height:329px;background:var(--panel)}
.dev-title{left:0;top:663px;width:762px;text-align:center;font-family:"Josefin Sans",Arial,sans-serif;font-weight:600;font-size:22px;color:#222}
.dev-title span{color:var(--plum)}
.card{top:713px;width:170px;height:221px;background:var(--white)}
.card-head{height:39px;border-bottom:1px solid var(--plum);display:flex;align-items:center;justify-content:center;text-align:center;font-family:"Josefin Sans",Arial,sans-serif;font-weight:600;font-size:12.4px;line-height:14px;color:var(--plum);padding:0 10px}
.card-icon{position:absolute;left:53px;top:53px;width:64px;height:64px;border-radius:50%;background:var(--plum);display:flex;align-items:center;justify-content:center}
.card-text{position:absolute;left:18px;top:133px;width:134px;text-align:center;font-size:7.2px;line-height:11px;color:var(--muted)}
.card-btn{position:absolute;left:0;bottom:0;width:170px;height:28px;border-radius:0;font-size:8.4px}

.video{left:0;top:972px;width:762px;height:193px;background:linear-gradient(100deg,#3a3a46 0%,#262c3c 40%,#1c2233 100%)}
.video-title{left:92px;top:1014px;font-family:"Josefin Sans",Arial,sans-serif;font-size:22px;color:var(--white)}
.video-text{left:92px;top:1050px;width:370px;font-size:7.4px;line-height:14.4px;color:var(--white)}
.video-btn{left:88px;top:1102px;width:97px;height:24px;background:var(--plum-dark);font-size:10.4px;border-radius:0}
.play{left:497px;top:1041px}

.site-footer{left:0;top:1165px;width:762px;height:35px;background:var(--plum)}
.copyright{left:30px;top:1176px;font-size:7.4px;color:var(--white)}
.social{right:40px;top:1177px;display:flex;gap:15px;align-items:center}
.social .link-box{display:block;width:9px;height:9px;border:1.5px solid var(--social);border-radius:2px}
</style>
</head>
<body>

<header class="site-header abs"></header>
<nav class="util-links abs"><a>About Us</a><a>Contact Us</a><a>Blog</a></nav>
<div class="brand abs"><div class="brand-mark"></div><div class="brand-name">Fenwick Holdings Corporation</div></div>

<nav class="main-nav abs">
  <a class="active">HOME</a>
  <a>REAL ESTATE DEVELOPMENTS</a>
  <a>REAL ESTATE SALES</a>
  <a>MAPS</a>
  <a>VACATION RENTALS</a>
  <a>PROPERTY OWNER RESOURCES</a>
</nav>

<div class="hero abs" role="img" aria-label="Photograph of a sunny residential street with craftsman homes, green lawns and a couple riding bicycles"></div>
<div class="hero-title abs">COPPER RIDGE</div>
<div class="hero-arrows abs">
  <svg width="8" height="10" viewBox="0 0 8 10"><path d="M6 1 2 5l4 4" fill="none" stroke="#222" stroke-width="1.5"/></svg>
  <svg width="8" height="10" viewBox="0 0 8 10"><path d="M2 1l4 4-4 4" fill="none" stroke="#222" stroke-width="1.5"/></svg>
</div>

<h1 class="welcome-title abs">WELCOME TO<span>FENWICK-HOLDINGS</span></h1>
<p class="welcome-text abs">Central Oregon real estate developer Fenwick Holdings Corporation has created some of Central Oregon’s most recognizable real estate communities, including Westgate Cross-ing, Canyon Rim, Riverbend, Alder Butte, Alder Glen, Summit Pines Village Resort, and Copper Ridge in Prineville.</p>
<a class="btn welcome-btn abs">READ MORE</a>

<section class="developments abs"></section>
<h2 class="dev-title abs">Real Estate <span>Developments</span></h2>

<article class="card abs" style="left:26px">
  <div class="card-head">COPPER RIDGE</div>
  <div class="card-icon"><svg width="28" height="34" viewBox="0 0 28 34"><path d="M14 0 4 12h5L2 21h7L0 30h12v4h4v-4h12l-9-9h7l-7-9h5z" fill="#fff"/></svg></div>
  <p class="card-text">A walkable Prineville neighborhood of craftsman homes, tree-lined streets and parks close to the historic downtown.</p>
  <a class="btn card-btn">READ MORE</a>
</article>
<article class="card abs" style="left:203px">
  <div class="card-head">SUMMIT PINES VILLAGE RESORT</div>
  <div class="card-icon"><svg width="30" height="26" viewBox="0 0 30 26"><path d="M15 1 1 13l2 2 12-10 12 10 2-2-5-4V3h-3v3z" fill="#fff"/><path d="M6 15v10h7v-6h4v6h7V15L15 7z" fill="#fff"/></svg></div>
  <p class="card-text">Forested lodging and condominiums along the river, minutes from the mountain's lifts, trails and village shops.</p>
  <a class="btn card-btn">READ MORE</a>
</article>
<article class="card abs" style="left:382px">
  <div class="card-head">CANYON RIM</div>
  <div class="card-icon"><svg width="28" height="28" viewBox="0 0 28 28"><path d="M14 2 26 8v12l-12 6-12-6V8z" fill="none" stroke="#fff" stroke-width="3"/><path d="M2 8l12 6 12-6M14 14v12" fill="none" stroke="#fff" stroke-width="2"/></svg></div>
  <p class="card-text">Spacious homesites perched above the river canyon with sweeping Cascade views and direct access to open space.</p>
  <a class="btn card-btn">READ MORE</a>
</article>
<article class="card abs" style="left:559px">
  <div class="card-head">WESTGATE CROSSING</div>
  <div class="card-icon"><svg width="28" height="28" viewBox="0 0 28 28"><path d="M26 2 17 11M17 4v7h7M2 26l9-9M11 24v-7H4" fill="none" stroke="#fff" stroke-width="3"/></svg></div>
  <p class="card-text">An award-winning mixed-use community blending homes, shops, schools and parks on the west side of town.</p>
  <a class="btn card-btn">READ MORE</a>
</article>

<section class="video abs" role="img" aria-label="Dimmed photograph of a hand holding a solar panel"></section>
<h2 class="video-title abs">VIDEO</h2>
<p class="video-text abs">See how Fenwick Holdings has shaped Central Oregon for more than five decades, building smart, healthy and livable communities that celebrate natural beauty, local character and the outdoor lifestyle our neighbors love. Watch stories from residents, partners and the team.</p>
<a class="btn video-btn abs">VIEW ALL</a>
<svg class="play abs" width="54" height="54" viewBox="0 0 54 54"><circle cx="27" cy="27" r="24" fill="none" stroke="#8a8a8a" stroke-width="4"/><path d="M21 16v22l17-11z" fill="#8a8a8a"/></svg>

<footer class="site-footer abs"></footer>
<p class="copyright abs">All Rights Reserved. Copyrights @company Name. 2016</p>
<div class="social abs">
  <svg class="feed-icon" width="10" height="10" viewBox="0 0 10 10" aria-label="News feed"><circle cx="1.5" cy="8.5" r="1.5" fill="#fff"/><path d="M0 4.5A5.5 5.5 0 0 1 5.5 10M0 1a9 9 0 0 1 9 9" fill="none" stroke="#fff" stroke-width="1.6"/></svg>
  <span class="link-box" aria-label="Social link"></span>
  <span class="link-box" aria-label="Social link"></span>
  <span class="link-box" aria-label="Social link"></span>
  <span class="link-box" aria-label="Social link"></span>
</div>

</body>
</html>
```